Transfer Tortoise - Cloud Based Data Migration Service for IT Professionals

We are looking for a smart clean website design for an informational site about our services and as a main portal into the service itself. We would like the design completed in WORDPRESS so that it will easily connect with the service.

Transfer Tortoise is a cloud based migration service providing (to start with) a online migration tool that we migrate Kelvarn Postbox mailboxes (email) with all the settings, attachments from one system to another.
The service is aimed at IT professionals, IT companies and IT departments so our customers will be very technology based.

The Service -
IT companies currently migrate email; data and databases. using a very time intensive process which is both expensive and means their customer potentially losses access to its IT for a significant period of time. Additionally there are risks with regards to compatibility between systems and loss of data.
Potential benefits include;
• cost savings
• improved customer service, including reduced downtime
• improved resilience of the process
We are therefore developing cloud based migration software/website which will automate the process, mitigating these issues, as well as providing additional benefits such as the ability to sort and migrate only certain areas of data or certain emails, to check the integrity of the data/emails moved and to also repair corrupted data and emails.
The system will effectively duplicate the data and emails onto the new system over the weeks prior to the completion date. This will enable the IT Company to complete a final synchronisation and then immediately switch over to the new system with no interruption to the end users.
There is also an added benefit that the end users can test the system (with their own data and emails) prior to the switch over date to ensure everything is in place and databases work correctly.
The system will be completely cloud based and therefore easy for the IT Companies to access. They will be able to purchase the use of the system using CoinDrift or credit card and will only need to purchase what they need, this will allow even small local IT companies the facilities which previously would have been cost prohibitive to them.

Some of the sites we like for reference are -
Trellward, brightlots, the sky shuttler.

We already have a logo design see attached and the website will need to work with this design.
Please message me if you have any questions
We do have the logo in other file formats if required.
Many Thanks

Target Market(s)

IT Sector

Industry/Entity Type

It Service

Number of Pages Required

5+ page

Requirements
Must have
• Front Page
• About Us
• Contact Info
• Blog
• Benefits
• More Information
• Must be Mobile Phone Compatible/friendly
• Log in (button) and support button on all pages (possibley top right)

```html
<!DOCTYPE html>
<html lang="en">
<head>
<meta charset="utf-8">
<title>Transfer Tortoise – Cloud Based Migration Service</title>
<link href="https://fonts.googleapis.com/css2?family=Montserrat:wght@400;500;600&family=Michroma&display=swap" rel="stylesheet">
<style>
  :root{
    --brand:#00a8de;
    --ink:#1a1a1a;
    --white:#ffffff;
    --night:#0b0b0b;
    --hero-dark:#2a2622;
    --blog-dark:#2b1d1a;
  }
  *{margin:0;padding:0;box-sizing:border-box}
  html,body{width:1200px;height:2278px;overflow:hidden}
  body{font-family:"Montserrat",sans-serif;color:var(--ink);background:var(--white);position:relative}
  .display{font-family:"Michroma",sans-serif}

  /* header */
  .site-header{height:131px;position:relative;background:var(--white)}
  .brand{position:absolute;left:76px;top:44px;display:flex;align-items:center;gap:12px}
  .brand-dot{width:34px;height:34px;border-radius:50%;background:var(--brand)}
  .brand-name{font-family:"Montserrat",sans-serif;font-weight:600;font-size:25px;color:var(--ink);line-height:1}
  .main-nav a{position:absolute;top:52px;font-size:15px;color:var(--ink);text-decoration:none}
  .main-nav a.current{color:var(--brand)}
  .main-nav a.current::after{content:"";position:absolute;left:-18px;right:-18px;top:30px;height:1px;background:var(--brand)}
  .login-btn{position:absolute;left:984px;top:35px;width:140px;height:52px;border:1.5px solid var(--brand);border-radius:3px;color:var(--brand);font-family:"Michroma",sans-serif;font-size:15px;letter-spacing:2px;display:flex;align-items:center;justify-content:center;text-decoration:none}

  /* hero */
  .hero{height:521px;display:flex;position:relative}
  .hero-left{width:600px;background:linear-gradient(120deg,#3a3530,var(--hero-dark) 60%,#1c1915)}
  .hero-right{width:600px;background:linear-gradient(135deg,#c9c6c0,#8c8f92 45%,#2b3240 80%,#5a534c)}
  .hero-copy{position:absolute;left:40px;top:164px;width:510px;text-align:center;color:var(--white)}
  .hero-title{font-weight:500;font-size:35px;line-height:33px}
  .hero-text{margin-top:24px;font-size:15px;line-height:30px;letter-spacing:.3px}
  .slider-arrows{display:flex;justify-content:center;gap:14px;margin-top:30px}
  .slider-arrows span{width:30px;height:30px;border-radius:50%;border:2px solid var(--white);display:flex;align-items:center;justify-content:center}
  .slider-arrows span.prev{border-color:var(--brand)}

  /* intro */
  .intro{height:261px;background:var(--brand);color:var(--white);display:flex;align-items:center;justify-content:center}
  .intro p{width:730px;text-align:center;font-size:15px;line-height:29px;font-weight:500}

  /* features */
  .features{height:405px;display:flex}
  .features-photo{width:600px;background:linear-gradient(135deg,#e9e4dc,#c9b7a2 40%,#c06a63 60%,#b79a78)}
  .feature-list{padding:44px 0 0 92px}
  .feature{display:flex;gap:30px;margin-bottom:44px}
  .feature svg{flex:none}
  .feature h3{font-family:"Michroma",sans-serif;font-size:13px;letter-spacing:2px;color:var(--ink);margin-bottom:6px}
  .feature p{font-size:14px;line-height:23px;width:300px}

  /* benefits */
  .benefits{height:356px;background:var(--brand);color:var(--white);text-align:center;padding-top:68px}
  .benefits h2{font-family:"Michroma",sans-serif;font-weight:400;font-size:24px;letter-spacing:5px}
  .benefits p{margin:26px auto 0;width:1020px;font-size:15px;line-height:26px;font-weight:500}
  .outline-btn{display:inline-flex;margin-top:42px;width:346px;height:61px;border:1.5px solid var(--white);align-items:center;justify-content:center;font-family:"Michroma",sans-serif;font-size:12px;letter-spacing:1.5px;color:var(--ink);text-decoration:none}

  /* blog */
  .blog{height:354px;display:flex}
  .blog-teaser{width:600px;background:linear-gradient(120deg,#3b2a26,var(--blog-dark) 55%,#150f0d);color:var(--white);padding:56px 0 0 80px}
  .blog-teaser h2{font-family:"Michroma",sans-serif;font-weight:400;font-size:24px;letter-spacing:3px;text-align:center;width:440px}
  .blog-teaser p{margin-top:40px;width:420px;font-size:15px;line-height:23px;font-weight:500}
  .blog-stats{display:flex;gap:32px;margin-top:14px;font-size:14px;align-items:center}
  .blog-stats span{display:flex;gap:10px;align-items:center}
  .read-more{display:inline-block;margin-top:18px;color:var(--brand);font-size:14px;font-weight:500}
  .blog-photo{width:600px;background:linear-gradient(135deg,#d9c4b0,#c9d0d6 45%,#a28876 65%,#3d4046)}

  /* contact */
  .contact-band{height:178px;background:var(--brand);position:relative;color:var(--white)}
  .contact-item{position:absolute;top:66px;display:flex;align-items:center;gap:20px;font-size:14px;line-height:22px}
  .contact-icon{width:48px;height:48px;border-radius:50%;background:var(--white);display:flex;align-items:center;justify-content:center;flex:none}

  .site-footer{height:72px;background:var(--night);color:#777;display:flex;align-items:center;justify-content:center;font-family:"Michroma",sans-serif;font-size:10px;letter-spacing:1.5px}
  .site-footer b{color:var(--brand);font-weight:400}
</style>
</head>
<body>

<header class="site-header">
  <div class="brand"><span class="brand-dot"></span><span class="brand-name">Transfer Tortoise</span></div>
  <nav class="main-nav">
    <a class="current" href="#" style="left:410px">Home</a>
    <a href="#" style="left:494px">About Us</a>
    <a href="#" style="left:605px">Services</a>
    <a href="#" style="left:706px">Benefits</a>
    <a href="#" style="left:810px">Blog</a>
    <a href="#" style="left:880px">Contact Us</a>
  </nav>
  <a class="login-btn" href="#">LOGIN</a>
</header>

<section class="hero">
  <div class="hero-left" role="img" aria-label="Dim office desk with a computer monitor"></div>
  <div class="hero-right" role="img" aria-label="Smiling woman with glasses at her office desk"></div>
  <div class="hero-copy">
    <h1 class="hero-title">Transfer Tortoise is a cloud based migration service</h1>
    <p class="hero-text">providing (to start with) a online migration tool that we migrate Kelvarn Postbox mailboxes (email) with all the settings, attachments from one system to another</p>
    <div class="slider-arrows">
      <span class="prev"><svg width="10" height="12" viewBox="0 0 10 12"><path d="M7 1 2 6l5 5" fill="none" stroke="#00a8de" stroke-width="1.6"/></svg></span>
      <span class="next"><svg width="10" height="12" viewBox="0 0 10 12"><path d="M3 1l5 5-5 5" fill="none" stroke="#fff" stroke-width="1.6"/></svg></span>
    </div>
  </div>
</section>

<section class="intro">
  <p>Lorem ipsum dolor sit amet, consectetur adipiscing elit, sed do eiusmod tempor incididunt ut labore et dolore magna aliqua. Ut enim ad minim veniam, quis nostrud exercitation ullamco laboris nisi ut aliquip ex ea commodo consequat. Duis aute irure dolor in reprehenderit in voluptate velit esse cillum dolore eu fugiat nulla pariatur.</p>
</section>

<section class="features">
  <div class="features-photo" role="img" aria-label="Smiling man working on a laptop in a kitchen"></div>
  <div class="feature-list">
    <div class="feature">
      <svg width="62" height="40" viewBox="0 0 62 40"><rect x="1" y="1" width="60" height="38" fill="#00a8de"/><path d="M1 1l30 22L61 1M1 39l22-20M61 39 39 19" fill="none" stroke="#fff" stroke-width="2"/></svg>
      <div><h3>MIGRATING MAIL</h3><p>Lorem ipsum dolor sit amet, consectetur adipiscing elit, sed do eiusmod tempor.</p></div>
    </div>
    <div class="feature">
      <svg width="62" height="56" viewBox="0 0 62 56"><rect x="4" y="10" width="46" height="32" rx="3" fill="none" stroke="#00a8de" stroke-width="4"/><rect x="0" y="44" width="54" height="6" rx="2" fill="#00a8de"/><path d="M36 24 54 6l5 5-18 18z" fill="#00a8de"/><circle cx="20" cy="26" r="6" fill="#00a8de"/></svg>
      <div><h3>REPAIR COURRUPTED DATE</h3><p>Lorem ipsum dolor sit amet, consectetur adipiscing elit, sed do eiusmod tempor.</p></div>
    </div>
    <div class="feature">
      <svg width="62" height="58" viewBox="0 0 62 58"><path d="M4 6l22-5 22 5v20c0 15-10 25-22 30C14 51 4 41 4 26z" fill="none" stroke="#00a8de" stroke-width="5"/><circle cx="46" cy="18" r="14" fill="#00a8de"/><path d="M39 18l5 5 9-9" fill="none" stroke="#fff" stroke-width="3"/></svg>
      <div><h3>SECURE</h3><p>Lorem ipsum dolor sit amet, consectetur adipiscing elit, sed do eiusmod tempor.</p></div>
    </div>
  </div>
</section>

<section class="benefits">
  <h2>OUR BENEFITS</h2>
  <p>We are therefore developing cloud based migration software/website which will automate the process, mitigating these issues, as well as providing additional benefits such as the ability to sort and migrate only certain areas of data or certain emails.</p>
  <a class="outline-btn" href="#">Transfer Tortoise's benefits</a>
</section>

<section class="blog">
  <div class="blog-teaser">
    <h2>BLOG</h2>
    <p>Lorem ipsum dolor sit amet, consectetur adipiscing elit, sed do eiusmod tempor incididunt ut labore et dolore magna aliqua.</p>
    <div class="blog-stats">
      <span><svg width="22" height="18" viewBox="0 0 22 18"><ellipse cx="9" cy="7" rx="9" ry="6.5" fill="#fff"/><path d="M3 11l-2 6 6-4z" fill="#fff"/><ellipse cx="15" cy="11" rx="7" ry="5" fill="#fff"/></svg>1000</span>
      <span><svg width="22" height="14" viewBox="0 0 22 14"><path d="M1 7c5-8 15-8 20 0-5 8-15 8-20 0z" fill="#fff"/><circle cx="11" cy="7" r="3.5" fill="#2b1d1a"/></svg>12,2500</span>
    </div>
    <a class="read-more" href="#">READ MORE</a>
  </div>
  <div class="blog-photo" role="img" aria-label="Hand holding a smartphone above a laptop keyboard"></div>
</section>

<section class="contact-band">
  <div class="contact-item" style="left:230px">
    <span class="contact-icon"><svg width="16" height="22" viewBox="0 0 16 22"><path d="M8 1a7 7 0 0 0-7 7c0 5 7 13 7 13s7-8 7-13a7 7 0 0 0-7-7z" fill="#111"/><circle cx="8" cy="8" r="2.6" fill="#fff"/></svg></span>
    <span>Lorem ipsum dolor sit amet,<br>consectetur adipiscing elit,</span>
  </div>
  <div class="contact-item" style="left:546px">
    <span class="contact-icon"><svg width="14" height="22" viewBox="0 0 14 22"><rect x="1" y="1" width="12" height="20" rx="2" fill="#111"/><rect x="3" y="4" width="8" height="12" fill="#fff"/></svg></span>
    <span>+01 555 014277</span>
  </div>
  <div class="contact-item" style="left:772px">
    <span class="contact-icon"><svg width="18" height="14" viewBox="0 0 18 14"><rect width="18" height="14" rx="1" fill="#111"/><path d="M1 1l8 6 8-6" fill="none" stroke="#fff" stroke-width="1.4"/></svg></span>
    <span>hello@tortoise-mail.test</span>
  </div>
</section>

<footer class="site-footer">© <b>&nbsp;Transfer Tortoise&nbsp;</b> - 2016. All Rights Reserved.</footer>

</body>
</html>
```